POLITICAL CARD TO HAND OUT

A LITTLE LARGER THAN THE REGULAR BUSINESS CARD WITH THE ABOVE INFORMATION.

Industry/Entity Type

Business

Contact Information for Business Card

ELECT *DEAN MARLOW* FOR JUSTICE OF THE PEACE PCT 6-EXPERIENCED LEADERSHIP- WITH MY PICTURE ON IT- PHONE 281-555-3816-REPUBLICAN PRIMARY - EARLY VOTING FEB 18TH THRU FEB 28 AND ELECTION DAY IS MARCH 4TH, 2014- USE RED WHITE AND BLUE WITH SOME STARS.

Requirements
Must have
• A FIVE POINTED STAR ON EACH SIDE OF MY NAME

```html
<!DOCTYPE html>
<html lang="en">
<head>
<meta charset="utf-8">
<title>Dean Marlow for Justice of the Peace – Campaign Card</title>
<link rel="stylesheet" href="https://fonts.googleapis.com/css2?family=Oswald:wght@500;700&family=Michroma&family=Tinos&family=Didact+Gothic&display=swap">
<style>
  :root {
    --backdrop: #d9d9d9;
    --card-white: #ffffff;
    --ink: #141414;
    --campaign-red: #d42027;
    --band-red: #d3222a;
    --navy-top: #26348f;
    --navy-deep: #1b2474;
    --star-gold: #c9a13a;
    --star-light: #ecd27a;
    --text-white: #ffffff;
    --heading-dark: #0c0f2e;
  }
  * { margin: 0; padding: 0; box-sizing: border-box; }
  html, body { width: 1200px; height: 900px; overflow: hidden; }
  body {
    background: var(--backdrop);
    display: flex;
    align-items: center;
    justify-content: center;
  }
  .campaign-card {
    position: relative;
    width: 1100px;
    height: 620px;
    background: var(--card-white);
    overflow: hidden;
    box-shadow: 0 10px 30px rgba(0,0,0,0.25);
  }
  .card-bands {
    position: absolute;
    inset: 0;
    width: 100%;
    height: 100%;
  }
  .headline {
    position: absolute;
    top: 36px;
    left: 0;
    width: 100%;
    display: flex;
    align-items: center;
    justify-content: center;
    gap: 8px;
    white-space: nowrap;
    font-family: "Oswald", sans-serif;
    font-weight: 700;
    color: var(--ink);
    text-transform: uppercase;
  }
  .headline-word { font-size: 40px; line-height: 1; padding-top: 10px; }
  .candidate-name {
    font-size: 64px;
    line-height: 1;
    color: var(--campaign-red);
  }
  .name-star { width: 46px; height: 46px; margin-top: 6px; }
  .tagline {
    position: absolute;
    top: 122px;
    left: 450px;
    white-space: nowrap;
    font-family: "Michroma", sans-serif;
    font-size: 21px;
    color: var(--campaign-red);
    letter-spacing: 2px;
    -webkit-text-stroke: 0.6px var(--campaign-red);
  }
  .phone-line {
    position: absolute;
    top: 303px;
    left: 460px;
    display: flex;
    gap: 70px;
    white-space: nowrap;
    font-family: "Michroma", sans-serif;
    font-size: 26px;
    color: var(--text-white);
    letter-spacing: 4px;
  }
  .candidate-photo {
    position: absolute;
    left: 14px;
    top: 140px;
    width: 420px;
    height: 480px;
    border-radius: 180px 180px 0 0;
    background: linear-gradient(180deg, #e8e0cf 0%, #d6b79c 30%, #3a3535 58%, #1b1b1f 100%);
  }
  .election-info {
    position: absolute;
    left: 470px;
    top: 392px;
    width: 600px;
    text-align: center;
  }
  .primary-title {
    font-family: "Tinos", serif;
    font-size: 42px;
    font-weight: 400;
    color: var(--heading-dark);
    letter-spacing: 1px;
    margin-bottom: 26px;
    white-space: nowrap;
  }
  .voting-dates {
    font-family: "Didact Gothic", sans-serif;
    font-size: 29px;
    line-height: 1.32;
    color: var(--text-white);
    white-space: nowrap;
  }
</style>
</head>
<body>
  <main class="campaign-card">
    <svg class="card-bands" viewBox="0 0 1100 620" preserveAspectRatio="none" aria-hidden="true">
      <defs>
        <linearGradient id="navyFill" x1="0" y1="0" x2="0" y2="1">
          <stop offset="0" stop-color="var(--navy-top)"/>
          <stop offset="1" stop-color="var(--navy-deep)"/>
        </linearGradient>
      </defs>
      <polygon points="0,330 1100,288 1100,620 0,620" fill="var(--band-red)"/>
      <polygon points="0,362 1100,352 1100,620 0,620" fill="url(#navyFill)"/>
    </svg>

    <h1 class="headline">
      <span class="headline-word">Elect</span>
      <svg class="name-star" viewBox="0 0 100 100" aria-hidden="true">
        <polygon points="50,4 61,38 97,38 68,59 79,94 50,73 21,94 32,59 3,38 39,38" fill="var(--star-gold)" stroke="var(--star-light)" stroke-width="2"/>
      </svg>
      <span class="candidate-name">Dean Marlow</span>
      <svg class="name-star" viewBox="0 0 100 100" aria-hidden="true">
        <polygon points="50,4 61,38 97,38 68,59 79,94 50,73 21,94 32,59 3,38 39,38" fill="var(--star-gold)" stroke="var(--star-light)" stroke-width="2"/>
      </svg>
      <span class="headline-word">For Justice of the Peace</span>
    </h1>

    <p class="tagline">PCT 6-EXPERIENCED LEADERSHIP</p>

    <p class="phone-line"><span>PHONE</span><span>281-555-3816</span></p>

    <div class="candidate-photo" role="img" aria-label="Portrait photo of the candidate in a white cowboy hat, dark suit and patterned tie"></div>

    <section class="election-info">
      <h2 class="primary-title">REPUBLICAN&nbsp; PRIMARY</h2>
      <p class="voting-dates">EARLY VOTING FEB 18TH THRU FEB 28<br>AND<br>ELECTION DAY IS MARCH 4TH, 2014</p>
    </section>
  </main>
</body>
</html>
```